****FLYER design - LAW FIRM ADVERTISEMENT****

We are a small law firm based in Los Angeles, CA. We need an flyer used for advertising that we will be passing out. We want the flyer to be about 4in x 6in.

We want the flyer to advertise the name of our firm: MORVANTE KELDRIC LLP (no period)
- We want our group photo to take up a good portion of the flyer (although it's okay if parts of the photo have wording over it.)

COLORS: Our firm colors are different shades of steal/metal grey with a bit of a bold orange accent. Any bold writing, like our slogan, names of practice areas,... should be in orange.

We envision a horizontal lay-out of the flyer, but are open to creative options laid out vertically!

Feel free to play with the fonts, the sizing, the color combinations,...

We want the flyer to advertise our two areas of practice: PERSONAL INJURY and EMPLOYMENT LAW. Please also place each photo icon of our areas of practice somewhere around the name (ambulance photo for personal injury; person behind computer desk for employment law). The icons can be relatively small.

Under Personal Injury, please write:
If you or a loved one are suffering from an injury or wrongful death caused by the careless or intentional acts of others, then you have the right to pursue compensation for your injury, out-of-pocket expenses, lost wages, emotional anguish, and more.

Under Employment Law, please write:
Our attorneys regularly represent clients in disputes involving sex, age and race discrimination, sexual harassment, retaliatory discharge, defamation, unlawful termination, breach of employment contracts, and more.

Somewhere on the flyer, please write our slogan IN ITALICS (and probably in orange):
- You Speak. We Listen. They Pay.

In somewhat bright and bold writing, please write "CONTACT US FOR A FREE CONSULTATION TODAY!" (maybe just after our slogan?)
- And under that phrase, write:
- 731 W. Larkmoor Avenue, Suite 400 Glenfield, CA 90488
phone: 555.318.9062
fax: 555.318.9074
email: info@mkrlegal-example.com
web: www.mkrlegal-example.com

If possible, and only if there's room without it looking too busy, somewhere in the upper left corner, place our "MKR" logo.
Updates

PLEASE NOTE THAT WE CHANGED OUR GROUP PHOTO TO A SLIGHTLY EDITED ONE.  PLEASE BE SURE TO USE THE NEW ONE!!!  (We deleted the old.)

Target Market(s)

employees, lower and mid-income individuals, minority communities. However, we still want the flyer to look sleek, modern, and professional.

Industry/Entity Type

Advertising

Requirements
Must have
• Firm Name,
Photo of Partners,
Names, photos, and small description of practice areas,
Firm slogan,
"Contact us for a free consultation today!",
Firm contact info.

And only if space and overall look permits, firm "MKR" logo.

We want an overall very sleek, modern feel to our flyer. While we do want to look professional, we wanted a more approachable feel than the typical, conservative law offices.
Nice to have
• Firm "MKR" logo

Horizontal lay out, though we're open to vertical options.

```html
<!DOCTYPE html>
<html lang="en">
<head>
<meta charset="utf-8">
<title>Morvante Keldric LLP – Flyer</title>
<link href="https://fonts.googleapis.com/css2?family=Fira+Sans+Condensed:ital,wght@0,400;0,500;0,600;0,700;1,600;1,700&display=swap" rel="stylesheet">
<style>
  :root{
    --steel:#5d6873;
    --steel-dark:#4a545e;
    --steel-light:#c9c9ce;
    --orange:#e07b24;
    --ink:#4a545e;
    --white:#ffffff;
    --black:#000000;
    --muted:#b9bec4;
  }
  *{box-sizing:border-box;margin:0;padding:0}
  html,body{width:1200px;height:1200px;overflow:hidden;background:var(--white)}
  body{position:relative;font-family:"Fira Sans Condensed",Arial,sans-serif;color:var(--ink)}
  .card{position:absolute;overflow:hidden;background:var(--white)}

  /* front */
  .front{left:152px;top:56px;width:780px;height:521px;background:var(--steel-light)}
  .front__photo{position:absolute;left:0;top:0;width:684px;height:419px;
    background:linear-gradient(135deg,#6e5a3e 0%,#a88a5e 35%,#3c4a3a 70%,#8d7a5c 100%)}
  .front__title-band{position:absolute;left:0;top:419px;width:684px;height:87px;background:var(--steel);text-align:center;padding-top:10px}
  .front__firm{color:var(--white);font-weight:700;font-size:34px;letter-spacing:.3px;line-height:1.1}
  .front__tagline{color:var(--muted);font-weight:500;font-size:20px;line-height:1.3}
  .front__accent{position:absolute;left:0;top:506px;width:684px;height:15px;background:var(--orange)}
  .front__icon{position:absolute;left:694px;width:86px;height:86px;background:var(--black);display:flex;align-items:center;justify-content:center}
  .front__icon--injury{top:226px}
  .front__icon--employment{top:323px}
  .front__mark{position:absolute;left:694px;top:419px;width:86px;height:87px;background:var(--steel);display:flex;align-items:center;justify-content:center;color:var(--white);font-weight:500;font-size:22px;letter-spacing:4px}

  /* back */
  .back{left:266px;top:618px;width:780px;height:518px;border:1px solid #d9d9d9}
  .practice{position:absolute;top:46px;width:330px}
  .practice--injury{left:46px}
  .practice--employment{left:406px}
  .practice__head{display:flex;align-items:flex-end;gap:8px;height:87px}
  .practice__icon{width:86px;height:86px;background:var(--black);display:flex;align-items:center;justify-content:center;flex:none}
  .practice__name{color:var(--orange);font-weight:600;font-size:27px;line-height:1;margin-bottom:-2px;white-space:nowrap}
  .practice__text{margin-top:16px;font-weight:600;font-size:14.6px;line-height:1.38;color:var(--ink)}
  .slogan{position:absolute;left:0;top:318px;width:780px;height:46px;background:var(--orange);color:var(--white);
    font-style:italic;font-weight:600;font-size:24px;text-align:center;line-height:46px}
  .contact{position:absolute;left:0;top:364px;width:780px;height:140px;background:linear-gradient(var(--steel-dark),var(--steel))}
  .contact__cta{color:var(--white);font-weight:500;font-size:25px;text-align:center;margin-top:14px}
  .contact__details{position:absolute;left:203px;top:58px;width:376px;color:var(--white);font-weight:500;font-size:15px;line-height:20px}
  .contact__row{display:flex;justify-content:space-between}
  .back__accent{position:absolute;left:0;bottom:0;width:780px;height:14px;background:var(--orange)}
</style>
</head>
<body>

<section class="card front">
  <div class="front__photo" role="img" aria-label="Group photo of the three firm partners standing in an office lobby"></div>
  <div class="front__title-band">
    <h1 class="front__firm">MORVANTE KELDRIC LLP</h1>
    <p class="front__tagline">Personal Injury and Employment Law</p>
  </div>
  <div class="front__accent"></div>
  <div class="front__icon front__icon--injury">
    <svg width="60" height="40" viewBox="0 0 60 40" aria-label="Ambulance icon">
      <path d="M2 8h34v24H2z M36 14h12l8 10v8H36z" fill="#fff"/>
      <path d="M40 17h7l5 7H40z" fill="#000"/>
      <path d="M16 12h6v6h6v6h-6v6h-6v-6h-6v-6h6z" fill="#000"/>
      <circle cx="13" cy="33" r="5" fill="#fff" stroke="#000" stroke-width="2"/>
      <circle cx="45" cy="33" r="5" fill="#fff" stroke="#000" stroke-width="2"/>
    </svg>
  </div>
  <div class="front__icon front__icon--employment">
    <svg width="50" height="50" viewBox="0 0 50 50" aria-label="Person at desk icon">
      <rect x="4" y="10" width="12" height="10" fill="#fff"/>
      <rect x="2" y="22" width="24" height="3" fill="#fff"/>
      <rect x="8" y="25" width="3" height="20" fill="#fff"/>
      <circle cx="32" cy="9" r="5" fill="#fff"/>
      <path d="M27 16h10v14h6v15h-4V34h-9z" fill="#fff"/>
      <path d="M28 18l-8 6 2 2 8-5z" fill="#fff"/>
    </svg>
  </div>
  <div class="front__mark">MKR</div>
</section>

<section class="card back">
  <article class="practice practice--injury">
    <div class="practice__head">
      <div class="practice__icon">
        <svg width="60" height="40" viewBox="0 0 60 40" aria-label="Ambulance icon">
          <path d="M2 8h34v24H2z M36 14h12l8 10v8H36z" fill="#fff"/>
          <path d="M40 17h7l5 7H40z" fill="#000"/>
          <path d="M16 12h6v6h6v6h-6v6h-6v-6h-6v-6h6z" fill="#000"/>
          <circle cx="13" cy="33" r="5" fill="#fff" stroke="#000" stroke-width="2"/>
          <circle cx="45" cy="33" r="5" fill="#fff" stroke="#000" stroke-width="2"/>
        </svg>
      </div>
      <h2 class="practice__name">PERSONAL INJURY</h2>
    </div>
    <p class="practice__text">If you or a loved one are suffering from an injury or wrongful death caused by the careless or intentional acts of others, then you have the right to pursue compensation for your injury, out-of-pocket expenses, lost wages, emotional anguish, and more.</p>
  </article>

  <article class="practice practice--employment">
    <div class="practice__head">
      <div class="practice__icon">
        <svg width="50" height="50" viewBox="0 0 50 50" aria-label="Person at desk icon">
          <rect x="4" y="10" width="12" height="10" fill="#fff"/>
          <rect x="2" y="22" width="24" height="3" fill="#fff"/>
          <rect x="8" y="25" width="3" height="20" fill="#fff"/>
          <circle cx="32" cy="9" r="5" fill="#fff"/>
          <path d="M27 16h10v14h6v15h-4V34h-9z" fill="#fff"/>
          <path d="M28 18l-8 6 2 2 8-5z" fill="#fff"/>
        </svg>
      </div>
      <h2 class="practice__name">EMPLOYMENT LAW</h2>
    </div>
    <p class="practice__text">Our attorneys regularly represent clients in disputes involving sex, age and race discrimination, sexual harassment, retaliatory discharge, defamation, unlawful termination, breach of employment contracts, and more.</p>
  </article>

  <p class="slogan">YOU SPEAK. WE LISTEN. THEY PAY.</p>

  <div class="contact">
    <p class="contact__cta">Contact us for a free consultation today</p>
    <div class="contact__details">
      <p>731 W. Larkmoor Avenue, Suite 400 Glenfield, CA 90488</p>
      <p class="contact__row"><span>phone: 555.318.9062</span><span>email: info@mkrlegal-example.com</span></p>
      <p class="contact__row"><span>fax: 555.318.9074</span><span>web: www.mkrlegal-example.com</span></p>
    </div>
  </div>
  <div class="back__accent"></div>
</section>

</body>
</html>
```